4x6 -ish post card to let the neighborhood know where here.

Hi All, I opened a high end wine & spirits shop and am looking to get out some sort of a 4x6 postcard a flyer to let people know where in the area. Looking for something clean cut that can maybe incorporate a few pictures from our store on along the top and our logo. Ideally a white-ish background.

```html
<!DOCTYPE html>
<html lang="en">
<head>
<meta charset="utf-8">
<title>Alderbrook Wine &amp; Spirits – Postcard</title>
<link href="https://fonts.googleapis.com/css2?family=Poppins:ital,wght@0,400;0,500;0,600;0,700;1,300&family=Great+Vibes&family=Roboto+Condensed:wght@400;600&family=Arimo:wght@400;700&display=swap" rel="stylesheet">
<style>
  :root{
    --backdrop:#ffffff;
    --brown:#3a2f2a;
    --gold:#c08a2e;
    --white:#ffffff;
    --ink:#1e1e1e;
    --rule:#3b3b3b;
  }
  *{margin:0;padding:0;box-sizing:border-box;}
  html,body{width:1094px;height:1200px;overflow:hidden;background:var(--backdrop);}
  body{position:relative;font-family:'Poppins',sans-serif;}

  .card{position:absolute;width:720px;height:480px;overflow:hidden;}
  .card--front{left:189px;top:84px;background:var(--brown);}
  .card--back{left:185px;top:618px;background:var(--white);}

  .photo{position:absolute;}
  .photo--tasting{left:0;top:0;width:405px;height:480px;
    background:linear-gradient(90deg,#b33a3f 0%,#c4505a 30%,#9a4f4a 55%,#6a4538 78%,var(--brown) 100%);}
  .photo--shelves{left:0;top:0;width:510px;height:480px;
    background:linear-gradient(90deg,#141414 0%,#2a2a2a 45%,rgba(120,120,120,.6) 75%,rgba(255,255,255,0) 100%);}

  .brand{position:absolute;font-family:'Poppins',sans-serif;font-weight:500;line-height:1;}
  .brand__name{display:block;letter-spacing:.5px;}
  .brand__sub{display:block;}
  .brand--front{left:438px;top:112px;width:222px;color:var(--white);}
  .brand--front .brand__name{font-size:33px;}
  .brand--front .brand__sub{font-size:17px;letter-spacing:3.4px;margin-top:8px;}

  .front-copy{position:absolute;left:412px;width:256px;text-align:center;}
  .tagline-script{top:194px;font-family:'Great Vibes',cursive;font-size:66px;color:var(--gold);line-height:1;}
  .tagline-gold{top:264px;font-size:29px;color:var(--gold);line-height:1;}
  .tagline-big{top:292px;font-size:62px;font-weight:500;color:var(--white);line-height:1;letter-spacing:1px;}
  .tagline-sub{top:352px;font-size:20px;font-weight:600;color:var(--white);line-height:1;letter-spacing:.5px;}

  .cta{position:absolute;left:439px;top:398px;width:211px;height:32px;border-radius:16px;
    background:var(--gold);color:var(--white);font-size:16px;line-height:32px;text-align:center;}
  .cta b{font-weight:700;}

  .return-address{position:absolute;right:128px;top:46px;text-align:right;font-style:normal;
    font-family:'Roboto Condensed',sans-serif;color:var(--ink);font-size:17px;line-height:20px;}
  .return-address strong{font-weight:600;font-size:17.5px;}

  .postage{position:absolute;left:608px;top:41px;width:75px;height:75px;border:1px solid var(--rule);
    font-family:'Arimo',sans-serif;font-size:10px;line-height:12px;text-align:center;padding-top:6px;color:var(--ink);}
  .postage b{font-weight:700;}

  .mail-box{position:absolute;left:511px;top:134px;width:172px;height:69px;border:1px solid var(--rule);
    font-family:'Arimo',sans-serif;font-size:10px;line-height:11px;color:var(--ink);}
  .mail-box__route{position:absolute;right:12px;top:7px;font-size:8px;}
  .mail-box__name{position:absolute;left:12px;top:30px;}

  .brand--back{right:37px;top:284px;color:var(--gold);}
  .brand--back .brand__name{font-size:30px;}
  .brand--back .brand__sub{font-size:16px;letter-spacing:3px;margin-top:6px;color:var(--gold);}

  .contact{position:absolute;right:35px;text-align:right;color:var(--gold);line-height:1;}
  .contact--phone{top:368px;font-size:23px;}
  .contact--phone i{font-style:italic;font-weight:300;}
  .contact--phone b{font-weight:700;}
  .contact--web{top:397px;font-size:21px;}
  .contact--web b{font-weight:700;}
</style>
</head>
<body>

<section class="card card--front" aria-label="Postcard front">
  <div class="photo photo--tasting" role="img" aria-label="Photo of a smiling woman in a red blouse tasting a glass of red wine in the shop"></div>
  <div class="brand brand--front">
    <span class="brand__name">ALDERBROOK</span>
    <span class="brand__sub">WINE &amp; SPIRITS</span>
  </div>
  <p class="front-copy tagline-script">Premium</p>
  <p class="front-copy tagline-gold">WINES &amp; SPIRITS</p>
  <p class="front-copy tagline-big">NOW IN</p>
  <p class="front-copy tagline-sub">YOUR NEIGHBORHOOD</p>
  <div class="cta"><b>ALDERBROOK</b>WINE.COM</div>
</section>

<section class="card card--back" aria-label="Postcard back">
  <div class="photo photo--shelves" role="img" aria-label="Photo of the store's wine shelves and angled bottle racks with price tags"></div>
  <address class="return-address">
    <strong>Alderbrook Wine &amp; Spirits</strong><br>
    42 Harbor View Road<br>
    Easton, CT, US 06612
  </address>
  <div class="postage">PRSRT STD<br>ECRWSS<br>U.S. Postage<br><b>PAID</b><br>EDDM RETAIL</div>
  <div class="mail-box">
    <span class="mail-box__route">******************ECRWSS****</span>
    <span class="mail-box__name">Local<br>Postal Customer</span>
  </div>
  <div class="brand brand--back">
    <span class="brand__name">ALDERBROOK</span>
    <span class="brand__sub">WINE &amp; SPIRITS</span>
  </div>
  <p class="contact contact--phone"><i>CALL US</i> <b>555.010.2030</b></p>
  <p class="contact contact--web"><b>ALDERBROOK</b>WINE.COM</p>
</section>

</body>
</html>
```